Company service wheel graphic

A graphic demonstrating all the services the company offers.
I have hand drawn and written up on the attached the content that is required. Also attached is our company logo so you have a sense of the colour scheme of the logo.
This will eventually go into a company brochure, be used on our website etc.

Target Market(s)

Local GOvernment and other professionals who work in the sport, recreation and leisure industries

Industry/Entity Type

Sports, recreation, leisure, aquatics

Font styles to use
Other font styles liked:
• Calibri

Colors
0054AA
0677BA
7BADD7
CADEEF
E8F1F8

Requirements
Must have
• An eye catching graphic that captures all the information in the hand drawn atachement.
Nice to have
• Each quadrant in the circle to have its own colour, that links to the company logo

```html
<!DOCTYPE html>
<html lang="en">
<head>
<meta charset="utf-8">
<title>Service Wheel</title>
<link rel="stylesheet" href="https://fonts.googleapis.com/css2?family=Source+Sans+3:wght@400;600;700&display=swap">
<style>
  :root {
    --planning: #29235f;
    --management: #1077bd;
    --participation: #7bacd7;
    --outcomes: #0055aa;
    --hub: #003c7d;
    --label-box: #0054aa;
    --frame-line: #b9d3ee;
    --ink-light: #ffffff;
    --ink-dark: #29235f;
    --page: #ffffff;
  }
  html, body {
    margin: 0;
    padding: 0;
    width: 1200px;
    height: 1200px;
    overflow: hidden;
    background: var(--page);
  }
  .service-wheel {
    display: block;
    width: 1200px;
    height: 1200px;
    font-family: "Source Sans 3", "Calibri", sans-serif;
  }
  .quadrant-planning { fill: var(--planning); }
  .quadrant-management { fill: var(--management); }
  .quadrant-participation { fill: var(--participation); }
  .quadrant-outcomes { fill: var(--outcomes); }
  .audience-ring {
    fill: var(--ink-dark);
    font-size: 26px;
    font-weight: 600;
    letter-spacing: 2.2px;
  }
  .service-list {
    fill: var(--ink-light);
    font-size: 17px;
    font-weight: 400;
    letter-spacing: 1.5px;
  }
  .frame-line {
    fill: none;
    stroke: var(--frame-line);
    stroke-width: 1.5;
  }
  .label-box {
    fill: var(--label-box);
    stroke: var(--frame-line);
    stroke-width: 1.5;
  }
  .box-title {
    fill: var(--ink-light);
    font-size: 20px;
    font-weight: 700;
    letter-spacing: 1.2px;
  }
  .stage-label {
    fill: var(--ink-light);
    font-size: 17px;
    font-weight: 700;
    letter-spacing: 1.6px;
  }
  .hub-circle { fill: var(--hub); }
  .hub-title {
    fill: var(--ink-light);
    font-size: 23px;
    font-weight: 700;
    letter-spacing: 2px;
  }
</style>
</head>
<body>
<svg class="service-wheel" viewBox="0 0 1200 1200" xmlns="http://www.w3.org/2000/svg">
  <defs>
    <path id="arc-top" d="M 112 600 A 488 488 0 0 1 1088 600"/>
    <path id="arc-bottom" d="M 87 600 A 513 513 0 0 0 1113 600"/>
  </defs>

  <!-- Quadrants -->
  <path class="quadrant-planning" d="M600 600 L118 600 A482 482 0 0 1 600 118 Z"/>
  <path class="quadrant-management" d="M600 600 L600 118 A482 482 0 0 1 1082 600 Z"/>
  <path class="quadrant-outcomes" d="M600 600 L1082 600 A482 482 0 0 1 600 1082 Z"/>
  <path class="quadrant-participation" d="M600 600 L600 1082 A482 482 0 0 1 118 600 Z"/>

  <!-- Audience ring -->
  <text class="audience-ring">
    <textPath href="#arc-top" startOffset="49%" text-anchor="middle">LOCAL + STATE GOVERNMENT • SPORT + LEISURE FACILITY MANAGERS</textPath>
  </text>
  <text class="audience-ring">
    <textPath href="#arc-bottom" startOffset="50%" text-anchor="middle">INVESTORS, DEVELOPERS,ARCHITECTS + DESIGNERS • SPORT, RECREATION + COMMUNITY PROVIDERS</textPath>
  </text>

  <!-- Planning services -->
  <text class="service-list">
    <tspan x="404" y="188">• Feacibility studies</tspan>
    <tspan x="335" y="225">• Community + stakeholder</tspan>
    <tspan x="421" y="244">research</tspan>
    <tspan x="273" y="282">• Sport + recreation strategies</tspan>
    <tspan x="239" y="320">• Design strategies</tspan>
    <tspan x="209" y="357">• Indoor + outdoor spaces</tspan>
  </text>

  <!-- Management services -->
  <text class="service-list">
    <tspan x="612" y="175">• Activating</tspan>
    <tspan x="624" y="193">underutilised assets</tspan>
    <tspan x="612" y="222">• Income + revenue</tspan>
    <tspan x="624" y="240">generation strategies</tspan>
    <tspan x="612" y="269">• Mystery shopper + business</tspan>
    <tspan x="624" y="288">health checks</tspan>
    <tspan x="612" y="316">• Financial + funding strategies</tspan>
    <tspan x="612" y="344">• Management support</tspan>
    <tspan x="612" y="372">• Busines planning</tspan>
  </text>

  <!-- Participation services -->
  <text class="service-list">
    <tspan x="143" y="658">• Trends + insights</tspan>
    <tspan x="149" y="696">• Health profiling</tspan>
    <tspan x="160" y="733">• Active recreation</tspan>
    <tspan x="177" y="752">strategies</tspan>
    <tspan x="177" y="790">• Community</tspan>
    <tspan x="200" y="809">program</tspan>
    <tspan x="211" y="827">development</tspan>
    <tspan x="216" y="865">• Physical activity strategies</tspan>
    <tspan x="250" y="903">• Specific cohort strategies</tspan>
    <tspan x="284" y="941">• Sport + program</tspan>
    <tspan x="312" y="960">specific strategies</tspan>
  </text>

  <!-- Outcomes services -->
  <text class="service-list">
    <tspan x="804" y="669">• Community impact</tspan>
    <tspan x="821" y="689">monitoring</tspan>
    <tspan x="804" y="731">• Social value</tspan>
    <tspan x="804" y="773">• Community</tspan>
    <tspan x="821" y="793">outcomes + KPIs</tspan>
    <tspan x="770" y="835">• Contract monitoring</tspan>
  </text>

  <!-- Inner frame -->
  <rect class="frame-line" x="429" y="429" width="342" height="383"/>
  <rect class="label-box" x="351" y="388" width="498" height="41"/>
  <text class="box-title" x="600" y="415" text-anchor="middle">Community, aquatic + recreation facilities</text>
  <rect class="label-box" x="429" y="771" width="342" height="41"/>
  <text class="box-title" x="600" y="798" text-anchor="middle">Comunity activation</text>

  <!-- Stage labels -->
  <text class="stage-label" x="443" y="467">Planning</text>
  <text class="stage-label" x="634" y="466">Management</text>
  <text class="stage-label">
    <tspan x="443" y="736">Growing</tspan>
    <tspan x="443" y="755">participation</tspan>
  </text>
  <text class="stage-label" text-anchor="end">
    <tspan x="756" y="715">Community</tspan>
    <tspan x="718" y="734">impact +</tspan>
    <tspan x="750" y="753">outcomes</tspan>
  </text>

  <!-- Hub -->
  <circle class="hub-circle" cx="600" cy="600" r="107"/>
  <text class="hub-title" text-anchor="middle">
    <tspan x="600" y="565">Community</tspan>
    <tspan x="600" y="592">+</tspan>
    <tspan x="600" y="621">Stakeholder</tspan>
    <tspan x="600" y="649">Engagement</tspan>
  </text>
</svg>
</body>
</html>
```